Menu Design for Chocolate and Cheese Shop

We are chocolate (and cheese) makers - www.mintleafery.com.au and would like to redesign our café menu (attached is the pdf of the old one). I would like to end up with a file using Adobe suite of products so we can readily update menus as we change them. Clean, classy and inviting. We would also like to incorporate our cheese with our sister business into the menu offering (www.thistledalepasture.com.au and www.facebook.com/thistledalepasture). Just allow space for us to flesh out content for the cheese menu items - we will definitely include our Brie Hour in this if you see our facebook posts) - 4pp - A4 landscape folded into A5. We would also like the exact same menu but with our Thistledale Pasture Branding instead of mintleafery (we have two different sites -attached are our thistledale pasture logos as well for incorporating into the second document)

```html
<!DOCTYPE html>
<html lang="en">
<head>
<meta charset="utf-8">
<title>mintleafery chocolate – café menu</title>
<link rel="stylesheet" href="https://fonts.googleapis.com/css2?family=Fondamento&family=Oswald:wght@500&family=Libre+Franklin:wght@400&display=swap">
<style>
  :root {
    --paper: #f2e8dc;
    --panel: #3f3430;
    --panel-line: #f4ece2;
    --ink: #2b211c;
    --ink-soft: #3a2e28;
    --price: #7a4a1c;
    --heading: #5a3412;
    --panel-text: #e9ddcf;
    --panel-name: #efe3d3;
  }
  * { box-sizing: border-box; margin: 0; padding: 0; }
  html, body { width: 1200px; height: 849px; overflow: hidden; background: var(--paper); }
  .menu { position: relative; width: 1200px; height: 849px; background: var(--paper); overflow: hidden; }

  .spread-left, .spread-right { position: absolute; top: 0; height: 849px; background: var(--paper); }
  .spread-left { left: 0; width: 319px; }
  .spread-right { left: 592px; width: 608px; }
  .spine { position: absolute; left: 319px; top: 0; width: 273px; height: 849px; background: var(--panel); }

  .section-title {
    position: absolute; font-family: "Fondamento", cursive; color: var(--heading);
    font-size: 44px; line-height: 1; white-space: nowrap; transform: translateX(-50%);
    text-align: center;
  }
  .section-title--panel { color: #fbf6ef; font-size: 46px; }
  .section-title--kids { font-size: 40px; line-height: 50px; }

  .item { position: absolute; color: var(--ink); }
  .item-name { font-family: "Oswald", sans-serif; font-weight: 500; font-size: 15.5px; line-height: 17px; color: #1f1712; letter-spacing: 0.1px; }
  .item-desc {
    font-family: "Libre Franklin", sans-serif; font-size: 12.4px; line-height: 17.2px; color: var(--ink-soft);
    text-align: justify; text-align-last: left; margin-top: 1px;
  }
  .item-price {
    position: absolute; top: 0; font-family: "Oswald", sans-serif; font-weight: 500; font-size: 15.5px;
    line-height: 17px; color: var(--price); text-align: right; white-space: nowrap;
  }

  /* left page */
  .treat { left: 29px; width: 266px; }
  .treat .item-desc { width: 196px; }
  .treat .item-price { right: 0; }

  /* drinks */
  .drink { left: 608px; width: 272px; }
  .drink .item-desc { width: 196px; }
  .drink .item-price { right: 0; }
  .drink-alt { left: 900px; width: 272px; }
  .drink-alt .item-name, .drink-alt .item-desc { width: 196px; }
  .drink-alt .item-desc { width: 196px; }
  .drink-alt .item-price { right: 0; }
  .kids { left: 900px; width: 272px; }
  .kids .item-price { right: 0; }

  /* centre panel */
  .brand-box {
    position: absolute; left: 329px; top: -2px; width: 250px; height: 144px;
    border: 1.5px solid var(--panel-line); display: flex; align-items: center; justify-content: center; gap: 12px;
  }
  .brand-name { font-family: "Libre Franklin", sans-serif; font-size: 30px; color: #9c8b7d; letter-spacing: -0.5px; }
  .brand-mark { width: 22px; height: 22px; border-radius: 50%; background: #c9c09a; }
  .tasting-box {
    position: absolute; left: 329px; top: 165px; width: 250px; height: 700px; border: 1.5px solid var(--panel-line);
  }
  .tasting { position: absolute; left: 357px; width: 196px; text-align: center; }
  .tasting .item-name { color: var(--panel-name); }
  .tasting .item-desc { color: var(--panel-text); text-align: justify; text-align-last: left; }
  .tasting .item-price-inline { font-family: "Oswald", sans-serif; font-weight: 500; font-size: 15.5px; line-height: 20px; color: #fff; margin-top: 1px; }
</style>
</head>
<body>
<main class="menu">
  <section class="spread-left" aria-label="Sweet treats"></section>
  <section class="spine" aria-label="Brie Hour"></section>
  <section class="spread-right" aria-label="Drinks"></section>

  <h1 class="section-title" style="left:167px; top:58px;">Sweet Treats</h1>

  <div class="item treat" style="top:163px;">
    <h2 class="item-name">chocolate taste plate</h2>
    <p class="item-desc">chocolate macaron, chocolate ice cream, chocolate mousse, and oursignature chocolate</p>
    <span class="item-price">$14.30</span>
  </div>
  <div class="item treat" style="top:249px;">
    <h2 class="item-name">caramel taste plate</h2>
    <p class="item-desc">caramel slice, hokey pokey ice cream, caramel truffle, and alfa-jores (Spanish shortbread) filled with dulce de leche</p>
    <span class="item-price">$14.30</span>
  </div>
  <div class="item treat" style="top:352px;">
    <h2 class="item-name">raspberry brownie</h2>
    <p class="item-desc">Brownie topped with raspberries, served warm with a scoop of vanilla bean ice cream</p>
    <span class="item-price">$12.50</span>
  </div>
  <div class="item treat" style="top:437px;">
    <h2 class="item-name">ice cream sensation</h2>
    <p class="item-desc">a trio of chocolate ice cream or our weekly special ice cream servedwith chocolate sauce and sprinkled with dark crispy pearls (ask our team what flavour is available)</p>
    <span class="item-price">$12.00</span>
  </div>
  <div class="item treat" style="top:574px;">
    <h2 class="item-name">chocolate mousse</h2>
    <p class="item-desc" style="text-align:left;">rich and creamy chocolate mousse served with white crispy pearls</p>
    <span class="item-price">$12.00</span>
  </div>
  <div class="item treat" style="top:642px;">
    <h2 class="item-name">handmade chocolates</h2>
    <p class="item-desc" style="text-align:left;">choose from our extensive range of fresh chocolates and truffles</p>
    <span class="item-price">from $1.90</span>
  </div>
  <div class="item treat" style="top:711px;">
    <h2 class="item-name">dessert jars</h2>
    <p class="item-desc" style="text-align:left;">ask our team to find out what is on offer this week</p>
    <span class="item-price">$15.50</span>
  </div>
  <div class="item treat" style="top:779px;">
    <h2 class="item-name">handmade cookies</h2>
    <span class="item-price">$3.00</span>
  </div>

  <div class="brand-box">
    <span class="brand-name">mintleafery</span>
    <span class="brand-mark" aria-hidden="true"></span>
  </div>
  <div class="tasting-box"></div>
  <h1 class="section-title section-title--panel" style="left:455px; top:205px;">Brie Hour</h1>

  <div class="item tasting" style="top:283px;">
    <h2 class="item-name">chocolate taste plate</h2>
    <p class="item-desc">chocolate macaron, chocolate ice cream, chocolate mousse, and oursignature chocolate</p>
    <p class="item-price-inline">$14.30</p>
  </div>
  <div class="item tasting" style="top:403px;">
    <h2 class="item-name">caramel taste plate</h2>
    <p class="item-desc">caramel slice, hokey pokey ice cream, caramel truffle, and alfa-jores (Spanish shortbread) filled with dulce de leche</p>
    <p class="item-price-inline">$12.50</p>
  </div>
  <div class="item tasting" style="top:540px;">
    <h2 class="item-name">raspberry brownie</h2>
    <p class="item-desc">Brownie topped with raspberries, served warm with a scoop of vanilla bean ice cream</p>
    <p class="item-price-inline">$15.50</p>
  </div>
  <div class="item tasting" style="top:660px;">
    <h2 class="item-name">ice cream sensation</h2>
    <p class="item-desc">a trio of chocolate ice cream or our weekly special ice cream servedwith chocolate sauce and sprinkled with dark crispy pearls (ask our team what flavour is available)</p>
    <p class="item-price-inline">$15.50</p>
  </div>

  <h1 class="section-title" style="left:894px; top:58px;">Drinks</h1>

  <div class="item drink" style="top:163px;">
    <h2 class="item-name">hot chocolate</h2>
    <p class="item-desc">traditional – made with 65% maracaibo single origin chocolate white – made with white chocolate half and half – half traditional and half white hot chocolate</p>
    <span class="item-price">reg $5.50<br>lrg $6.00</span>
  </div>
  <div class="item drink" style="top:283px;">
    <h2 class="item-name">mocha</h2>
    <p class="item-desc">can be made with traditional or white chocolate</p>
    <span class="item-price">reg $6.00<br>lrg $6.50</span>
  </div>
  <div class="item drink" style="top:352px;">
    <h2 class="item-name">special hot chocolate</h2>
    <p class="item-desc">a creamy ganache made with crème fraiche infused with a different flavour each week (ask our team what flavour is available)</p>
    <span class="item-price">reg $6.50<br>lrg $7.00</span>
  </div>
  <div class="item drink" style="top:472px;">
    <h2 class="item-name">coffee</h2>
    <p class="item-desc">latte, cappuccino, flat white, long black, short black, short macchi-ato, long macchiato, piccolo latte</p>
    <span class="item-price">reg $4.00<br>lrg $4.50</span>
  </div>
  <div class="item drink" style="top:557px;">
    <h2 class="item-name">chai</h2>
    <span class="item-price">reg $4.00<br>lrg $4.50</span>
  </div>
  <div class="item drink" style="top:608px;">
    <h2 class="item-name">tea – a pot of leaf &amp; kettle<br>organic tea</h2>
    <p class="item-desc">english breakfast, earl grey, french earl grey, wellbeing, coco-nut, berry green, white tea and rose, chai, dark tea &amp; chocolate, lemongrass and ginger</p>
    <span class="item-price">$5.00</span>
  </div>
  <div class="item drink" style="top:745px;">
    <h2 class="item-name">affogato</h2>
    <p class="item-desc">vanilla bean icream served with a shot of coffee or molten chocolate</p>
    <span class="item-price">$6.00</span>
  </div>

  <div class="item drink-alt" style="top:163px;">
    <h2 class="item-name">iced coffee</h2>
    <span class="item-price">$5.50</span>
  </div>
  <div class="item drink-alt" style="top:197px;">
    <h2 class="item-name">iced chocolate<br>white or 65% maracaibo single origin chocolate</h2>
    <p class="item-desc">our special blend of greenvale cream, milk, and chocolate</p>
    <span class="item-price">$7.00</span>
  </div>
  <div class="item drink-alt" style="top:300px;">
    <h2 class="item-name">iced mocha<br>white or traditional -</h2>
    <span class="item-price">$7.50</span>
  </div>
  <div class="item drink-alt" style="top:352px;">
    <h2 class="item-name">milkshakes</h2>
    <p class="item-desc" style="text-align:left;">chocolate, (our own decadent fudge, vanilla or caramel)</p>
    <span class="item-price">$6.00</span>
  </div>
  <div class="item drink-alt" style="top:420px;">
    <h2 class="item-name" style="width:auto;">clearbrook – still or sparkling water</h2>
    <span class="item-price">$3.00</span>
  </div>

  <h1 class="section-title section-title--kids" style="left:1040px; top:484px;">For the<br>Children</h1>

  <div class="item kids" style="top:608px;"><h2 class="item-name">mini hot chocolate</h2><span class="item-price">$3.00</span></div>
  <div class="item kids" style="top:642px;"><h2 class="item-name">mini chino</h2><span class="item-price">$1.00</span></div>
  <div class="item kids" style="top:677px;"><h2 class="item-name">mini chino with teddy pop</h2><span class="item-price">$2.50</span></div>
  <div class="item kids" style="top:711px;"><h2 class="item-name">mini ice chocolate</h2><span class="item-price">$5.00</span></div>
  <div class="item kids" style="top:745px;"><h2 class="item-name">mini icecream</h2><span class="item-price">$3.50</span></div>
  <div class="item kids" style="top:779px;"><h2 class="item-name">mini mousse</h2><span class="item-price">$3.50</span></div>
</main>
</body>
</html>
```